Tidewell Recovery Business Card Design

Professional and clean design. The design colors should flow with the logo. Two-sided card with the website on the back which is:

www.TidewellRecovery.example.

"Specializing in Water Damage Restoration"

On the front I need the name, email, phone, and logo.

Name: Dorian Vashti
Email: Dorian@TidewellRecovery.example
Phone: 555-318-2046 for now

I only have the Preview and Thumbnail right now but should have the source files uploaded within a day or two.

Target Market(s)

Flood victims, home owners with water damage from busted pipes etc...

Industry/Entity Type

Business

Contact Information for Business Card

Name: Dorian Vashti

Font styles to use
Serif
Sans Serif

```html
<!DOCTYPE html>
<html lang="en">
<head>
<meta charset="utf-8">
<title>Tidewell Recovery Business Card</title>
<link href="https://fonts.googleapis.com/css2?family=Cinzel:wght@500;600&family=Open+Sans:wght@400;600&display=swap" rel="stylesheet">
<style>
  :root {
    --backdrop: #e6e6e4;
    --card-white: #ffffff;
    --band-light: #56bff0;
    --band-deep: #2596d6;
    --brand-blue: #2a8fd3;
    --text-on-band: #ffffff;
  }
  * { box-sizing: border-box; margin: 0; padding: 0; }
  html, body {
    width: 1200px; height: 1000px; overflow: hidden;
    background: var(--backdrop);
  }
  .canvas {
    width: 1200px; height: 1000px;
    display: flex; flex-direction: column; align-items: center; justify-content: center;
    gap: 60px;
  }
  .card {
    position: relative;
    width: 700px; height: 400px;
    border-radius: 22px;
    background: var(--card-white);
    overflow: hidden;
    box-shadow: 0 6px 18px rgba(0,0,0,0.18);
  }
  .brand {
    position: absolute; left: 0; right: 0; top: 44px;
    display: flex; flex-direction: column; align-items: center; gap: 16px;
  }
  .brand-dot {
    width: 96px; height: 96px; border-radius: 50%;
    background: var(--brand-blue);
  }
  .brand-name {
    font-family: "Cinzel", serif; font-weight: 600;
    font-size: 40px; letter-spacing: 2px;
    color: var(--brand-blue);
  }
  .band-light {
    position: absolute; left: 0; right: 0; top: 262px; height: 42px;
    background: var(--band-light);
    display: flex; align-items: center; justify-content: center;
    color: var(--text-on-band);
  }
  .band-deep {
    position: absolute; left: 0; right: 0; top: 304px; bottom: 0;
    background: var(--band-deep);
    display: flex; align-items: center; justify-content: center; gap: 40px;
    color: var(--text-on-band);
    font-family: "Open Sans", sans-serif; font-size: 20px; letter-spacing: 0.5px;
  }
  .holder-name {
    font-family: "Cinzel", serif; font-weight: 500;
    font-size: 26px; letter-spacing: 2px;
  }
  .tagline {
    font-family: "Open Sans", sans-serif; font-size: 18px; letter-spacing: 1px;
  }
  .contact { display: flex; align-items: center; gap: 10px; }
  .contact-badge {
    width: 26px; height: 26px; border-radius: 50%;
    border: 2px solid var(--band-light);
    color: var(--band-light);
    font-size: 14px; font-weight: 600;
    display: flex; align-items: center; justify-content: center;
  }
  .web-icon { width: 24px; height: 24px; }
</style>
</head>
<body>
<main class="canvas">
  <section class="card card-back" aria-label="Card back">
    <div class="brand">
      <div class="brand-dot"></div>
      <div class="brand-name">TIDEWELL RECOVERY</div>
    </div>
    <div class="band-light"><span class="tagline">“Specializing in Water Damage Restoration”</span></div>
    <div class="band-deep">
      <span class="contact">
        <svg class="web-icon" viewBox="0 0 24 24" aria-hidden="true">
          <circle cx="12" cy="12" r="10" fill="none" stroke="#ffffff" stroke-width="2"/>
          <path d="M2 12h20M12 2c3 3 3 17 0 20M12 2c-3 3-3 17 0 20" fill="none" stroke="#ffffff" stroke-width="1.5"/>
        </svg>
        www.TidewellRecovery.example
      </span>
    </div>
  </section>

  <section class="card card-front" aria-label="Card front">
    <div class="brand">
      <div class="brand-dot"></div>
      <div class="brand-name">TIDEWELL RECOVERY</div>
    </div>
    <div class="band-light"><span class="holder-name">DORIAN VASHTI</span></div>
    <div class="band-deep">
      <span class="contact"><span class="contact-badge">M</span>Dorian@TidewellRecovery.example</span>
      <span class="contact"><span class="contact-badge">E</span>555-318-2046</span>
    </div>
  </section>
</main>
</body>
</html>
```